Business card design needed

I need a business card design for a new online retail business based in Australia. I am unsure of the exact content of what I will be selling but it will be probably women's clothing, accessories, gym wear, gifts and maybe homeware linen. I am wanting a classy design that portrays the image of class/style/upmarket.

Target Market(s)

predominantely women - 20-50 age group

Industry/Entity Type

Retail

Contact Information for Business Card

Purely Lustre
Karen Whitlow
Director
ABN 73215548906
17 Harcourt Lane Dunmore Ridge NSW 2291
ph: +61 427 390 845
sales@purelylustre.com.au

Logo Text

I am open for suggestions here

Requirements
Must have
• The design must be both sides of the card

```html
<!DOCTYPE html>
<html lang="en">
<head>
<meta charset="utf-8">
<title>Purely Lustre – Business Card</title>
<link rel="stylesheet" href="https://fonts.googleapis.com/css2?family=Mulish:wght@400;700&display=swap">
<style>
  :root {
    --backdrop: #2b2b2d;
    --card-white: #f7f7f7;
    --panel-light: #dcdcdc;
    --panel-mid: #c6c6c6;
    --band-name: #b4b4b4;
    --band-wide: #c9c9c9;
    --accent-dark: #48484b;
    --ink: #3a3a3c;
    --ink-soft: #5a5a5d;
    --gold: #c9a233;
    --photo-light: #e4e6ea;
    --photo-mid: #b9bfc7;
    --photo-dark: #8e959e;
  }
  * { box-sizing: border-box; margin: 0; padding: 0; }
  html, body {
    width: 1200px; height: 900px; overflow: hidden;
    background: var(--backdrop);
    font-family: "Mulish", "Century Gothic", sans-serif;
  }
  .stage {
    width: 1200px; height: 900px;
    display: flex; flex-direction: column; align-items: center; justify-content: center;
    gap: 48px;
  }
  .card {
    position: relative;
    width: 620px; height: 372px;
    overflow: hidden;
    box-shadow: 0 10px 30px rgba(0,0,0,.45);
  }

  /* Photo side */
  .card--photo { background: var(--photo-mid); }
  .photo-fill {
    position: absolute; inset: 0;
    background: linear-gradient(120deg, var(--photo-light) 0%, var(--photo-mid) 55%, var(--photo-dark) 100%);
  }
  .photo-brand {
    position: absolute; right: 44px; top: 50%;
    transform: translateY(-50%);
    display: flex; align-items: center; gap: 12px;
  }
  .photo-brand__name {
    font-size: 38px; font-weight: 400; color: #ffffff; letter-spacing: .5px;
  }
  .photo-brand__dot {
    width: 16px; height: 16px; border-radius: 50%; background: var(--gold);
  }

  /* Contact side */
  .card--contact { background: var(--card-white); }
  .contact-panel {
    position: absolute; left: 16px; top: 16px; right: 16px; bottom: 16px;
    overflow: hidden;
    background: linear-gradient(180deg, var(--panel-light) 0%, var(--panel-mid) 100%);
  }
  .wide-band {
    position: absolute; left: 0; right: 0; top: 138px; height: 58px;
    background: var(--band-wide);
  }
  .name-band {
    position: absolute; left: 140px; top: 86px; width: 270px; height: 56px;
    background: var(--band-name);
    padding: 8px 0 0 24px;
  }
  .name-band__name { font-size: 21px; font-weight: 700; color: var(--ink-soft); line-height: 1.1; }
  .name-band__role { font-size: 15px; color: var(--ink-soft); }
  .accent-square {
    position: absolute; right: 0; top: 50px; width: 116px; height: 100px;
    background: var(--accent-dark);
  }
  .contact-brand {
    position: absolute; left: 40px; top: 44px;
    display: flex; align-items: center; gap: 8px;
  }
  .contact-brand__name { font-size: 24px; font-weight: 400; color: var(--ink); }
  .contact-brand__dot { width: 10px; height: 10px; border-radius: 50%; background: var(--gold); }

  .details {
    position: absolute; left: 40px; right: 24px; top: 232px;
    color: var(--ink); font-size: 15px;
    display: grid; grid-template-columns: auto 1fr; row-gap: 12px; column-gap: 18px;
  }
  .detail { display: flex; align-items: center; gap: 7px; white-space: nowrap; }
  .detail svg { width: 17px; height: 17px; fill: var(--ink-soft); flex: none; }
</style>
</head>
<body>
<main class="stage">
  <section class="card card--photo" aria-label="Card front">
    <div class="photo-fill" role="img" aria-label="Fashion photograph of legs in strappy heels stepping on a white staircase"></div>
    <div class="photo-brand">
      <span class="photo-brand__name">Purely Lustre</span>
      <span class="photo-brand__dot"></span>
    </div>
  </section>

  <section class="card card--contact" aria-label="Card back">
    <div class="contact-panel">
      <div class="wide-band"></div>
      <div class="name-band">
        <p class="name-band__name">Karen Whitlow</p>
        <p class="name-band__role">Director</p>
      </div>
      <div class="accent-square"></div>
      <div class="contact-brand">
        <span class="contact-brand__name">Purely Lustre</span>
        <span class="contact-brand__dot"></span>
      </div>

      <div class="details">
        <p class="detail">
          <svg viewBox="0 0 24 24" aria-hidden="true"><path d="M7 1h10a2 2 0 0 1 2 2v18a2 2 0 0 1-2 2H7a2 2 0 0 1-2-2V3a2 2 0 0 1 2-2zm0 3v12h10V4H7zm2 14v2h2v-2H9zm4 0v2h2v-2h-2z"/></svg>
          +61 427 390 845
        </p>
        <p class="detail">
          <svg viewBox="0 0 24 24" aria-hidden="true"><path d="M2 5h20v14H2V5zm2 2v.4l8 5.6 8-5.6V7H4zm0 2.8V17h16V9.8l-8 5.6-8-5.6z"/></svg>
          sales@purelylustre.com.au
        </p>
        <p class="detail">ABN 73215548906</p>
        <p class="detail">
          <svg viewBox="0 0 24 24" aria-hidden="true"><path d="M12 3l10 9h-3v9h-5v-6h-4v6H5v-9H2l10-9z"/></svg>
          17 Harcourt Lane Dunmore Ridge NSW 2291
        </p>
      </div>
    </div>
  </section>
</main>
</body>
</html>
```